Business Card Design Project

I need a business card for an environmentally friendly interior design company called Maplecrest Decor.
I was thinking it might be nice to print the business cards on brown recycled paper with green ink.
In addition to interior design, I will also be able to consult with homeowners regarding their indoor environments and how they might be affecting their health after May 2013 which is when I will complete my certification program. This can be added to the business card at that time: "Certified Dwelling Vitality Environmental Consultant".

```html
<!DOCTYPE html>
<html lang="en">
<head>
<meta charset="utf-8">
<title>Maplecrest Decor – Business Card</title>
<link href="https://fonts.googleapis.com/css2?family=Tinos:ital,wght@0,400;0,700;1,700&display=swap" rel="stylesheet">
<style>
  :root {
    --ink-deep: #22560f;
    --ink-leaf: #2a7a14;
    --mark-green: #2f8f1a;
    --paper-light: #d9a86a;
    --paper-mid: #c98d4e;
    --paper-dark: #a8692f;
  }
  html, body {
    margin: 0;
    padding: 0;
    width: 1200px;
    height: 670px;
    overflow: hidden;
    background: #ffffff;
  }
  .card {
    position: relative;
    width: 1200px;
    height: 670px;
    overflow: hidden;
    font-family: "Tinos", "Times New Roman", serif;
  }
  .paper-texture {
    position: absolute;
    inset: 0;
    background:
      radial-gradient(ellipse at 30% 35%, var(--paper-light) 0%, transparent 55%),
      radial-gradient(ellipse at 75% 60%, var(--paper-light) 0%, transparent 50%),
      linear-gradient(135deg, var(--paper-mid) 0%, var(--paper-light) 45%, var(--paper-mid) 75%, var(--paper-dark) 100%);
  }
  .text {
    position: absolute;
    margin: 0;
    white-space: nowrap;
    line-height: 1;
  }
  .company-heading {
    left: 70px;
    top: 74px;
    font-size: 34px;
    font-weight: 700;
    font-style: italic;
    color: var(--ink-deep);
    line-height: 47px;
  }
  .credential {
    left: 56px;
    top: 219px;
    font-size: 38px;
    font-weight: 700;
    color: var(--ink-deep);
  }
  .contact {
    left: 665px;
    top: 363px;
    width: 370px;
    text-align: center;
    font-weight: 700;
    color: var(--ink-deep);
  }
  .contact-name {
    font-size: 46px;
    display: block;
  }
  .contact-phone {
    font-size: 46px;
    display: block;
    margin-top: 16px;
  }
  .brand-square {
    position: absolute;
    left: 178px;
    top: 500px;
    width: 52px;
    height: 52px;
    background: var(--mark-green);
  }
  .brand-name {
    left: 253px;
    top: 503px;
    font-size: 56px;
    font-weight: 400;
    color: var(--ink-leaf);
  }
  .brand-tagline {
    left: 318px;
    top: 582px;
    font-size: 28px;
    font-weight: 400;
    color: var(--ink-deep);
  }
</style>
</head>
<body>
  <div class="card">
    <div class="paper-texture" role="img" aria-label="Crumpled brown recycled kraft paper texture"></div>

    <p class="text company-heading">Maplecrest Decor<br>Environmentally friendly design</p>

    <p class="text credential">Certified Dwelling Vitality Environmental Consultant</p>

    <p class="text contact">
      <span class="contact-name">Dana Lee Whitford</span>
      <span class="contact-phone">713-555-0148</span>
    </p>

    <div class="brand-square" aria-hidden="true"></div>
    <p class="text brand-name">Maplecrest Decor</p>
    <p class="text brand-tagline">for the green home</p>
  </div>
</body>
</html>
```